Website wordpress theme for brightwillowstudio.au

We need a modern dark mode website to entice customers to engage us to deliver web apps, mobile apps and VR apps. The site emphasises humans over tech.

Target Market(s)

Medium to large business and well funded startups

Industry/Entity Type

Information Technology

Coding

Coded - Design and coding required

Font styles to use
Sans Serif

Colors
EB3D1F
EC4F4E
F09395
F8D3D4
FCEDEE

Requirements
Must have
• Attractive image on home page

```html
<!DOCTYPE html>
<html lang="en">
<head>
<meta charset="utf-8">
<title>Bright Willow Studio</title>
<link rel="stylesheet" href="https://fonts.googleapis.com/css2?family=Poppins:wght@400;500;600;700&display=swap">
<style>
:root{
  --ink:#0b0b0d;
  --panel:#141418;
  --red:#c3121c;
  --red-deep:#8d0c13;
  --accent:#eb3d1f;
  --coral:#ec4f4e;
  --pink:#f09395;
  --blush:#f8d3d4;
  --white:#ffffff;
  --muted:#c9c9cf;
  --line:#5a5a62;
}
*{box-sizing:border-box;margin:0;padding:0}
html,body{width:1200px;height:3468px;overflow:hidden}
body{background:var(--ink);color:var(--white);font-family:'Poppins',sans-serif;position:relative}
.abs{position:absolute}
.btn{display:inline-block;background:var(--red);color:var(--white);font-size:13px;font-weight:600;letter-spacing:.5px;padding:10px 22px;border-radius:22px;text-transform:uppercase;white-space:nowrap}
.btn::after{content:" \00BB"}
.heading{font-size:36px;font-weight:700;text-align:center}
.small-bar{width:56px;height:4px;background:var(--red);border-radius:2px;position:absolute;left:572px}
.copy{font-size:14px;line-height:1.6;color:var(--muted)}
.photo{position:absolute;border-radius:4px}

/* header & hero */
.hero{left:0;top:0;width:1200px;height:760px;
  background:
    radial-gradient(circle at 63% 30%,rgba(255,236,200,.95) 0%,rgba(255,170,90,.55) 5%,rgba(120,170,230,.25) 14%,rgba(0,0,0,0) 26%),
    radial-gradient(ellipse at 75% 60%,rgba(150,175,200,.45) 0%,rgba(0,0,0,0) 40%),
    radial-gradient(ellipse at 40% 70%,rgba(90,120,160,.35) 0%,rgba(0,0,0,0) 45%),
    linear-gradient(180deg,#101a2a 0%,#0b1626 45%,#071019 100%)}
.hero-shade{left:0;top:0;width:1200px;height:760px;background:linear-gradient(90deg,rgba(5,8,14,.75) 0%,rgba(5,8,14,.35) 40%,rgba(5,8,14,0) 60%)}
.topbar{left:0;top:0;width:1200px;height:70px;background:linear-gradient(180deg,rgba(0,0,0,.75),rgba(0,0,0,0))}
.brand{left:96px;top:22px;display:flex;align-items:center;gap:10px;font-size:22px;font-weight:700;color:var(--white)}
.brand-mark{width:22px;height:22px;background:var(--red)}
.nav{left:560px;top:20px;display:flex;gap:40px;font-size:16px;font-weight:500;align-items:center}
.nav .btn{margin-left:10px;padding:9px 22px}
.hero-text{left:120px;top:280px;width:470px}
.hero-text h1{font-size:38px;font-weight:700;margin-bottom:12px}
.hero-text p{margin-bottom:26px;color:var(--white)}
.arrow{top:345px;font-size:44px;color:var(--white)}
.dots{left:566px;top:640px;display:flex;gap:10px}
.dots span{width:10px;height:10px;border-radius:50%;background:var(--muted)}
.dots span:first-child{background:var(--red)}

/* services */
.services{left:0;top:700px;width:1200px;height:640px;background:
  radial-gradient(ellipse at 20% 40%,rgba(40,46,60,.5),rgba(0,0,0,0) 55%),
  linear-gradient(#0d0f14,#121218)}
.cards{left:100px;top:850px;display:flex;gap:26px}
.card{width:316px;text-align:center}
.card .photo{position:static;height:220px;width:316px;display:block}
.card h3{font-size:24px;font-weight:600;margin:22px 0 8px}
.card .copy{margin-bottom:12px}
.card .btn{font-size:12px;padding:8px 18px}

/* welcome */
.welcome{left:0;top:1320px;width:1200px;height:600px;background:
  radial-gradient(ellipse at 70% 30%,rgba(120,130,150,.35),rgba(0,0,0,0) 55%),
  radial-gradient(ellipse at 15% 70%,rgba(70,80,100,.35),rgba(0,0,0,0) 50%),
  linear-gradient(90deg,#15161c,#22252e 60%,#131419)}
.welcome-mark{left:150px;top:1430px;width:300px;height:300px;border-radius:50%;background:radial-gradient(circle,rgba(195,18,28,.55),rgba(141,12,19,.35) 70%);}
.welcome-text{left:620px;top:1445px;width:490px}
.welcome-text h4{font-size:22px;font-weight:500}
.welcome-text h2{font-size:36px;font-weight:700;line-height:1.2}
.welcome-text .bar{width:200px;height:3px;background:var(--white);margin:14px 0 20px}
.welcome-text .copy{color:var(--white);margin-bottom:14px}

/* blog */
.blog{left:0;top:1880px;width:1200px;height:640px;background:var(--ink)}
.blog-item h3{font-size:22px;font-weight:600;line-height:1.3;margin-bottom:8px}
.blog-item .copy{margin-bottom:12px}
.blog-item .btn{font-size:12px;padding:8px 16px}

/* contact */
.contact{left:0;top:2500px;width:1200px;height:640px;background:
  radial-gradient(ellipse at 80% 30%,rgba(170,190,210,.35),rgba(0,0,0,0) 50%),
  radial-gradient(ellipse at 55% 80%,rgba(60,90,120,.35),rgba(0,0,0,0) 50%),
  linear-gradient(120deg,#090b10,#16202c 60%,#243446)}
.contact-shade{left:0;top:2500px;width:760px;height:640px;background:linear-gradient(90deg,rgba(6,8,12,.8),rgba(6,8,12,.2))}
.contact-text{left:100px;top:2630px;width:560px}
.contact-text h5{font-size:16px;font-weight:500}
.contact-text h2{font-size:40px;font-weight:700;margin-bottom:36px}
.fields{display:grid;grid-template-columns:1fr 1fr;gap:30px 30px}
.field{border-bottom:1px solid var(--line);padding-bottom:10px;font-size:14px;color:var(--muted)}
.field.wide{grid-column:1/3;height:80px}
.contact-text .btn{margin-top:40px;font-size:14px;padding:12px 26px}

/* footer */
.footer{left:0;top:3120px;width:1200px;height:348px;background:#0e0e11}
.footer-brand{left:100px;top:3180px;font-size:30px;font-weight:700;display:flex;align-items:center;gap:12px}
.footer-brand span.mark{width:28px;height:28px;background:var(--red)}
.socials{left:140px;top:3262px;display:flex;gap:14px}
.socials span{width:40px;height:40px;border:2px solid var(--white);border-radius:50%}
.col{top:3160px;font-size:14px;line-height:2}
.col h4{font-size:18px;font-weight:600;line-height:1.2;margin-bottom:10px}
.col p{color:var(--muted)}
.legal{left:0;top:3420px;width:1200px;height:48px;border-top:1px solid #2a2a30;text-align:center;line-height:48px;font-size:13px;color:var(--muted)}
</style>
</head>
<body>

<!-- hero -->
<section class="abs hero" role="img" aria-label="Robot hand and human hand reaching toward a glowing light bulb over a digital circuit background"></section>
<div class="abs hero-shade"></div>
<div class="abs topbar"></div>
<div class="abs brand"><span class="brand-mark"></span>Bright Willow Studio</div>
<nav class="abs nav">
  <span>Home</span><span>About</span><span>Our Services</span><span>Blog</span>
  <span class="btn">Contact Us</span>
</nav>
<div class="abs arrow" style="left:48px">&#8249;</div>
<div class="abs arrow" style="left:1124px">&#8250;</div>
<div class="abs hero-text">
  <h1>Bright Willow Studio</h1>
  <p class="copy">Lorem ipsum dolor sit amet, consectetur adipisicing elit, sed do eiusmod tempor incididunt ut labore et dolore magna aliqua.</p>
  <span class="btn">Get Started</span>
</div>
<div class="abs dots"><span></span><span></span><span></span><span></span></div>

<!-- services -->
<section class="abs services"></section>
<svg class="abs" style="left:0;top:640px" width="1200" height="160" viewBox="0 0 1200 160">
  <path d="M0 30 Q600 200 1200 30 L1200 0 L0 0Z" fill="#071019" opacity="0"/>
  <path d="M0 30 Q600 200 1200 30" stroke="var(--red)" stroke-width="10" fill="none"/>
</svg>
<div class="small-bar" style="top:782px"></div>
<h2 class="abs heading" style="left:0;width:1200px;top:790px">What We Do</h2>
<div class="abs cards">
  <div class="card">
    <div class="photo" role="img" aria-label="Developer working at multiple monitors showing code" style="background:radial-gradient(ellipse at 30% 35%,#3f86c8 0%,#1d4b7a 40%,#0c1d33 100%)"></div>
    <h3>Web Apps</h3>
    <p class="copy">Sed ut perspiciatis unde omnis iste natus error sit voluptatem accusantium, totam rem aperiam.</p>
    <span class="btn">Learn More</span>
  </div>
  <div class="card">
    <div class="photo" role="img" aria-label="Team of developers discussing work at a desk" style="background:radial-gradient(ellipse at 65% 45%,#8a93a3 0%,#3b4a60 45%,#121a26 100%)"></div>
    <h3>Mobile Apps</h3>
    <p class="copy">Sed ut perspiciatis unde omnis iste natus error sit voluptatem accusantium, totam rem aperiam.</p>
    <span class="btn">Learn More</span>
  </div>
  <div class="card">
    <div class="photo" role="img" aria-label="Person wearing a virtual reality headset" style="background:radial-gradient(ellipse at 55% 40%,#eef2f6 0%,#c9d2dc 40%,#7d8a9a 100%)"></div>
    <h3>VR Apps</h3>
    <p class="copy">Sed ut perspiciatis unde omnis iste natus error sit voluptatem accusantium, totam rem aperiam.</p>
    <span class="btn">Learn More</span>
  </div>
</div>

<!-- welcome -->
<section class="abs welcome" role="img" aria-label="Dim server room background"></section>
<svg class="abs" style="left:0;top:1270px" width="1200" height="120" viewBox="0 0 1200 120">
  <path d="M0 20 Q600 180 1200 20 L1200 0 L0 0Z" fill="#121218"/>
  <path d="M0 20 Q600 180 1200 20" stroke="var(--red)" stroke-width="10" fill="none"/>
</svg>
<div class="abs welcome-mark"></div>
<div class="abs welcome-text">
  <h4>WELCOME TO</h4>
  <h2>Bright Willow Studio</h2>
  <div class="bar"></div>
  <p class="copy">Lorem ipsum dolor sit amet, consectetur adipiscing elit, sed do eiusmod tempor incididunt ut labore et dolore magna. Quis ipsum suspendisse ultrices gravida maecenas accumsan lacus vel facilisis.</p>
  <p class="copy">Sed ut perspiciatis unde omnis iste natus error sit voluptatem accusantium doloremque laudantium, totam rem aperiam, eaque ipsa quae ab illo inventore veritatis.</p>
  <span class="btn">Learn More About Us</span>
</div>

<!-- blog -->
<section class="abs blog"></section>
<svg class="abs" style="left:0;top:1820px" width="1200" height="140" viewBox="0 0 1200 140">
  <path d="M0 100 Q600 -20 1200 100 L1200 140 L0 140Z" fill="var(--ink)"/>
  <path d="M0 100 Q600 -20 1200 100" stroke="var(--red)" stroke-width="10" fill="none"/>
</svg>
<div class="small-bar" style="top:1938px"></div>
<h2 class="abs heading" style="left:0;width:1200px;top:1950px">Latest Blog</h2>
<div class="photo" role="img" aria-label="Woman working with holographic data screens" style="left:100px;top:2012px;width:472px;height:250px;background:radial-gradient(ellipse at 70% 40%,#5fa6d8 0%,#203a5c 45%,#0b1320 100%)"></div>
<div class="abs blog-item" style="left:100px;top:2280px;width:472px">
  <h3>The standard Lorem Ipsum pass use the 1500s</h3>
  <p class="copy">Sed ut perspiciatis unde omnis iste natus error sit voluptatem accusantium doloremque laudantium, totam rem aperiam.</p>
  <span class="btn">Learn More</span>
</div>
<div class="photo" role="img" aria-label="Hands typing on a laptop" style="left:600px;top:2012px;width:192px;height:190px;background:radial-gradient(ellipse at 50% 40%,#d4dbe3 0%,#9aa6b4 45%,#4a5564 100%)"></div>
<div class="abs blog-item" style="left:820px;top:2020px;width:280px">
  <h3>The standard Lorem Ipsum pass use the 1500s</h3>
  <p class="copy">Sed ut perspiciatis unde omnis iste natus error sit voluptatem.</p>
  <span class="btn">Learn More</span>
</div>
<div class="photo" role="img" aria-label="Engineer working beside server racks" style="left:600px;top:2238px;width:192px;height:180px;background:radial-gradient(ellipse at 40% 45%,#e2e8ef 0%,#b6c2cf 40%,#56657a 100%)"></div>
<div class="abs blog-item" style="left:820px;top:2240px;width:280px">
  <h3>The standard Lorem Ipsum pass use the 1500s</h3>
  <p class="copy">Sed ut perspiciatis unde omnis iste natus error sit voluptatem.</p>
  <span class="btn">Learn More</span>
</div>

<!-- contact -->
<section class="abs contact" role="img" aria-label="Blurred modern office background"></section>
<div class="abs contact-shade"></div>
<div class="photo" role="img" aria-label="Smiling professional in a light shirt holding a laptop" style="left:800px;top:2540px;width:340px;height:580px;border-radius:0;background:radial-gradient(ellipse at 50% 55%,#dfe7ef 0%,#a9b9c9 35%,rgba(60,80,100,.2) 75%,rgba(0,0,0,0) 100%)"></div>
<svg class="abs" style="left:0;top:2460px" width="1200" height="140" viewBox="0 0 1200 140">
  <path d="M0 40 Q600 200 1200 40 L1200 0 L0 0Z" fill="var(--ink)"/>
  <path d="M0 40 Q600 200 1200 40" stroke="var(--red)" stroke-width="10" fill="none"/>
</svg>
<div class="abs contact-text">
  <h5>CONTACT US</h5>
  <h2>Get In Touch</h2>
  <div class="fields">
    <div class="field">Enter Your Name</div>
    <div class="field">Enter Your Email</div>
    <div class="field">Enter Your Number</div>
    <div class="field">Country</div>
    <div class="field wide">Tell us about your project</div>
  </div>
  <span class="btn">Submit Now</span>
</div>

<!-- footer -->
<footer class="abs footer"></footer>
<svg class="abs" style="left:0;top:3080px" width="1200" height="120" viewBox="0 0 1200 120">
  <path d="M0 80 Q600 0 1200 80 L1200 120 L0 120Z" fill="#0e0e11"/>
  <path d="M0 80 Q600 0 1200 80" stroke="var(--red)" stroke-width="10" fill="none"/>
</svg>
<div class="abs footer-brand"><span class="mark"></span>Bright Willow Studio</div>
<div class="abs socials"><span></span><span></span><span></span><span></span></div>
<div class="abs col" style="left:480px">
  <h4>Quick Link</h4>
  <p>Home</p><p>About Us</p><p>Services</p><p>Blog</p><p>Contact Us</p>
</div>
<div class="abs col" style="left:670px">
  <h4>Other Link</h4>
  <p>Privacy policy</p><p>Terms and condition</p><p>Sitemap</p><p>Help</p>
</div>
<div class="abs col" style="left:920px;width:240px">
  <h4>Contact Info</h4>
  <p>&#9906; 48 Willow Lane<br>&nbsp;&nbsp;&nbsp;Northbank, VIC 3006</p>
  <p>&#9742; +61 3 9000 1234</p>
  <p>&#9993; info@brightwillowstudio.au</p>
</div>
<div class="abs legal">Copyright &copy; 2023 &ndash; Bright Willow Studio. All Right Reserved</div>

</body>
</html>
```